Dodgeball League website

I require a nice, cool and attractive website for a new dodgeball league competition. I will need in PSD:

- Home Page
- Generic pages for news, about us etc
- Rank page with a table of team scores. stats etc

*Please design this with a Joomla*

I have attached:
- a logo
- site map for the links
- page layout guide

Example site for layout
http://www.velomarchcircuit.com/

Design
Retro,cool feel, matches well with logo

Contact me if you have any questions
Updates

Reason: Would like to see a few more designs

Target Market(s)

Young adults 18 - 35.

Industry/Entity Type

News

Colors

Designer to choose colors to be used in the design.

Requirements
Must have
• I want a cool, retro feel to the website. Not to picky on the colors. Something that will match nicely with the logo given. I will give feedback on it.
Calm colors not too bright and overwhelming
Nice to have
• Include some pictures within the picture slider so I can get a feel for the website.
Nice clean background
Should not have
• To much clutter of text
Do not put pictures in the background.

```html
<!DOCTYPE html>
<html lang="en">
<head>
<meta charset="utf-8">
<title>Harbour Dodge League</title>
<link href="https://fonts.googleapis.com/css2?family=Open+Sans:wght@400;600;700&family=Rokkitt:wght@700&display=swap" rel="stylesheet">
<style>
:root{
  --wood:#e3bd86;
  --wood-dark:#d3a96c;
  --bark:#5a3416;
  --bark-2:#7a4a20;
  --cream:#fbf3e2;
  --paper:#f3dfb8;
  --rust:#c0381a;
  --rust-dark:#8e2a12;
  --ink:#3c2f24;
  --muted:#6b5a48;
  --line:#e2d2b4;
  --sea:#1d5d7a;
  --sea-dark:#164a61;
  --frame:#efe3cb;
  --frame-edge:#cdb48a;
  --link-blue:#2f6fa3;
  --gold:#f2c53a;
}
*{box-sizing:border-box;margin:0;padding:0}
html,body{width:691px;height:1200px;overflow:hidden}
body{position:relative;font-family:"Open Sans",Arial,sans-serif;color:var(--ink);
  background:repeating-linear-gradient(90deg,var(--wood) 0 38px,var(--wood-dark) 38px 40px,#e8c692 40px 78px,var(--wood-dark) 78px 80px)}
.abs{position:absolute}
/* header */
.brand{left:64px;top:30px;width:124px;height:40px;display:flex;align-items:center;gap:6px}
.brand-dot{width:24px;height:24px;border-radius:50%;background:var(--rust);flex:none}
.brand-name{font-weight:700;font-size:12px;line-height:14px;color:var(--bark);white-space:nowrap}
.score{top:8px;width:104px;height:56px;background:var(--bark-2);border:3px solid var(--bark);border-radius:3px;color:#f6e6c8;font-size:6px;padding:4px 6px;box-shadow:0 2px 3px rgba(0,0,0,.3);white-space:nowrap}
.score .row{display:flex;justify-content:space-between;line-height:10px}
.score .row span:last-child{width:36px;display:flex;justify-content:space-between}
.nav{left:64px;top:77px;width:564px;height:27px;background:var(--bark-2);border-top:3px solid var(--bark);border-bottom:3px solid var(--bark);display:flex;align-items:center;justify-content:flex-end;padding-right:8px}
.nav a{color:#fff;text-decoration:none;font-size:9px;padding:2px 7px;margin-left:11px}
.nav a.active{background:var(--gold);color:var(--bark);font-weight:600}
/* hero */
.hero{left:64px;top:118px;width:564px;height:252px;transform:rotate(-.6deg);
  background:linear-gradient(180deg,var(--frame),#e6d5b6);border:1px solid var(--frame-edge);
  padding:12px;box-shadow:0 3px 6px rgba(0,0,0,.3)}
.hero-inner{width:100%;height:100%;background:#f7efe0}
.hero-photo{left:96px;top:145px;width:518px;height:198px;background:linear-gradient(120deg,#b7a995,#d9d2c7 45%,#8d8478);border:5px solid #fff;box-shadow:0 1px 3px rgba(0,0,0,.3)}
.ribbon{left:78px;top:140px;width:277px;height:38px;background:var(--sea);border:2px solid var(--sea-dark);transform:rotate(-1.5deg);display:flex;align-items:center;gap:8px;padding-left:10px;color:#fff;font-family:"Rokkitt",Georgia,serif;font-size:14px;box-shadow:0 2px 3px rgba(0,0,0,.3)}
.sticker{left:24px;top:174px;width:70px;height:82px;background:var(--paper);transform:rotate(-10deg);box-shadow:0 2px 4px rgba(0,0,0,.3);display:flex;align-items:center;justify-content:center}
.sticker span{width:42px;height:42px;border-radius:50%;background:var(--rust)}
/* main */
.panel{left:64px;top:392px;width:564px;height:788px;background:var(--cream);box-shadow:0 0 0 4px #efe0c2}
h2{font-size:11px;font-weight:600;color:var(--ink)}
.rule{height:1px;background:var(--line)}
.news{left:92px;width:352px;display:flex;gap:11px}
.news-img{width:89px;height:75px;border:3px solid #fff;box-shadow:0 1px 3px rgba(0,0,0,.35);flex:none}
.news h3{font-size:8px;font-weight:600;color:var(--rust);margin:1px 0 5px}
.news p{font-size:6.8px;line-height:9px;color:var(--muted);margin-bottom:4px}
.news .date{margin-bottom:1px}
.more{font-size:7px;color:var(--rust)}
.btn{background:var(--rust);color:#fff;border:2px solid var(--rust-dark);border-radius:3px;font-weight:600;text-align:center;white-space:nowrap}
.tab{top:684px;width:138px;height:21px;font-size:9.5px;line-height:17px}
.rank{left:99px;top:710px;width:345px;border-collapse:collapse;font-size:7.8px;color:var(--ink)}
.rank th{color:var(--rust);font-weight:400;text-align:left;height:21px;border-bottom:1px solid var(--line)}
.rank td{height:21.2px;border-bottom:1px solid var(--line)}
.rank td:first-child,.rank th:first-child{width:31px;text-align:center;border-right:1px solid var(--line)}
.rank td:last-child,.rank th:last-child{width:45px;text-align:center;border-left:1px solid var(--line)}
.rank td:nth-child(2),.rank th:nth-child(2){padding-left:8px}
.top3{top:950px;width:160px;height:94px;background:var(--paper);border:1px solid #d9bf90;box-shadow:0 2px 3px rgba(0,0,0,.25);padding:6px 6px}
.top3 h4{font-size:9.5px;font-weight:600;color:var(--ink);margin-bottom:6px}
.top3 table{width:100%;border-collapse:collapse;font-size:5.8px}
.top3 th{color:var(--rust);font-weight:400;text-align:left;height:12px;border-bottom:1px solid #d9bf90}
.top3 td{height:16px;border-bottom:1px solid #d9bf90}
.tape{width:30px;height:12px;background:rgba(190,170,130,.8)}
.sponsors{left:92px;top:1074px;width:518px;height:40px;display:flex;align-items:center;justify-content:space-between}
.sponsor{font-weight:700;font-size:11px;color:var(--ink);white-space:nowrap}
.foot{left:88px;top:1135px;width:528px;border-top:1px solid var(--line);padding-top:11px;display:flex;justify-content:space-between;font-size:7px;color:var(--muted)}
/* sidebar */
.like{left:474px;top:413px;width:120px;height:50px;text-align:center}
.like .tag{display:inline-block;background:var(--sea);color:#fff;font-size:8px;font-weight:700;letter-spacing:1px;padding:3px 10px}
.like .word{font-size:20px;font-weight:700;color:var(--link-blue);line-height:24px}
.register{left:458px;top:474px;width:152px;height:159px;background:#e9c98f;border:3px solid #c79a55;border-radius:8px;text-align:center;padding:10px 9px}
.register .kicker{color:var(--rust);font-size:8.5px}
.register .sub{font-size:8.5px;color:var(--ink);margin:2px 0 6px}
.register p{font-size:6px;line-height:8px;color:var(--muted);text-align:left;margin-bottom:6px}
.field{height:17px;border:1px solid #c7a46a;background:#f1dcb2;font-size:6px;color:var(--muted);text-align:left;padding:4px;margin-bottom:7px}
.register .btn{width:90px;height:17px;margin:2px auto 0;font-size:8px;line-height:13px}
.plugin{left:460px;top:648px;width:148px;height:136px;background:#fff;border:4px solid #efe6d6;box-shadow:0 1px 3px rgba(0,0,0,.25);padding:6px;font-size:6px;color:var(--muted)}
.plugin .ptitle{display:flex;gap:5px;align-items:center;color:var(--link-blue);font-size:7.5px}
.plugin .pdot{width:20px;height:20px;border-radius:50%;background:var(--rust);flex:none}
.avatars{display:grid;grid-template-columns:repeat(4,1fr);gap:3px 5px;margin-top:5px;text-align:center;font-size:5px}
.avatars i{display:block;height:24px;background:#b8c2cc}
.map-card{left:462px;top:800px;width:148px;height:128px;background:var(--sea);border-radius:4px;box-shadow:0 2px 4px rgba(0,0,0,.35)}
.map-head{left:474px;top:796px;width:132px;height:24px;background:var(--rust);color:#fff;font-size:9px;font-weight:600;padding:5px 12px}
.map-area{left:472px;top:822px;width:128px;height:96px;background:linear-gradient(135deg,#d9c49a,#b9a478 60%,#9bb0a8)}
</style>
</head>
<body>
<!-- header -->
<div class="abs brand"><span class="brand-dot"></span><span class="brand-name">Harbour Dodge<br>League</span></div>
<div class="abs score" style="left:190px"><div class="row"><span>Live Stream</span><span>Live Score</span></div><div class="row"><span></span><span><b>Pts</b><b>Sets</b></span></div><div class="row"><span>Team 1</span><span><b>2</b><b>2</b></span></div><div class="row"><span>Team 1</span><span><b>2</b><b>2</b></span></div></div>
<div class="abs score" style="left:301px"><div class="row"><span>Live Stream</span><span>Live Score</span></div><div class="row"><span></span><span><b>Pts</b><b>Sets</b></span></div><div class="row"><span>Team 1</span><span><b>2</b><b>2</b></span></div><div class="row"><span>Team 1</span><span><b>2</b><b>2</b></span></div></div>
<div class="abs score" style="left:412px"><div class="row"><span>Live Stream</span><span>Live Score</span></div><div class="row"><span></span><span><b>Pts</b><b>Sets</b></span></div><div class="row"><span>Team 1</span><span><b>2</b><b>2</b></span></div><div class="row"><span>Team 1</span><span><b>2</b><b>2</b></span></div></div>
<div class="abs score" style="left:523px"><div class="row"><span>Live Stream</span><span>Live Score</span></div><div class="row"><span></span><span><b>Pts</b><b>Sets</b></span></div><div class="row"><span>Team 1</span><span><b>2</b><b>2</b></span></div><div class="row"><span>Team 1</span><span><b>2</b><b>2</b></span></div></div>
<nav class="abs nav"><a class="active">Home</a><a>About Us</a><a>Teams</a><a>Schedule</a><a>News</a><a>Photos &amp; Videos</a><a>Register</a><a>Contact Us</a></nav>

<!-- hero -->
<div class="abs hero"><div class="hero-inner"></div></div>
<div class="abs hero-photo" role="img" aria-label="Players throwing dodgeballs in an indoor sports hall"></div>
<div class="abs ribbon"><svg width="20" height="20" viewBox="0 0 20 20"><polygon points="10,1 12.6,7.4 19.5,7.6 14,11.8 16,18.5 10,14.5 4,18.5 6,11.8 0.5,7.6 7.4,7.4" fill="#f0a52a"/></svg>Harbour Dodge League Sydney...</div>
<div class="abs sticker"><span></span></div>

<!-- main panel -->
<div class="abs panel"></div>
<h2 class="abs" style="left:88px;top:400px">Latest News</h2>
<div class="abs rule" style="left:88px;top:421px;width:356px"></div>

<article class="abs news" style="top:438px">
  <div class="news-img" role="img" aria-label="Player holding two red dodgeballs" style="background:linear-gradient(135deg,#9a7060,#c84a3c 55%,#5e4a42)"></div>
  <div><h3>Marcus Hale On Brink Of Qualifying</h3><p class="date">29.10.2013</p><p>Lorem ipsum dolor sit amet, consectetur adipisicing elit, sed do eiusmod tempor incididunt ut labore et dolore magna aliqua.</p><p>Ut enim ad minim veniam, quis nostrud exercitation ullamco laboris nisi ut aliquip ex ea commodo consequat....</p><span class="more">Read More »</span></div>
</article>
<div class="abs rule" style="left:88px;top:527px;width:356px"></div>
<article class="abs news" style="top:541px">
  <div class="news-img" role="img" aria-label="Player throwing a ball on a blue court" style="background:linear-gradient(135deg,#2c4f8f,#6a7fa8 55%,#c7523a)"></div>
  <div><h3>Marcus Hale On Brink Of Qualifying</h3><p class="date">29.10.2013</p><p>Lorem ipsum dolor sit amet, consectetur adipisicing elit, sed do eiusmod tempor incididunt ut labore et dolore magna aliqua.</p><p>Ut enim ad minim veniam, quis nostrud exercitation ullamco laboris nisi ut aliquip ex ea commodo consequat....</p><span class="more">Read More »</span></div>
</article>
<div class="abs rule" style="left:88px;top:630px;width:356px"></div>
<span class="abs more" style="left:412px;top:640px">View all »</span>

<h2 class="abs" style="left:88px;top:649px">Ranking Table</h2>
<div class="abs rule" style="left:88px;top:670px;width:356px"></div>
<div class="abs btn tab" style="left:125px">Ultimate Rubber Leage</div>
<div class="abs btn tab" style="left:270px">Ultimate Foam Leage</div>
<table class="abs rank">
  <tr><th>Rank</th><th>Team Name</th><th>Score</th></tr>
  <tr><td>01</td><td>Lorem ipsum dolor sit amet, consectetur adipsicing elit,</td><td>58</td></tr>
  <tr><td>02</td><td>Lorem ipsum dolor sit amet, consectetur adipsicing elit,</td><td>55</td></tr>
  <tr><td>03</td><td>Lorem ipsum dolor sit amet, consectetur adipsicing elit,</td><td>49</td></tr>
  <tr><td>04</td><td>Lorem ipsum dolor sit amet, consectetur adipsicing elit,</td><td>30</td></tr>
  <tr><td>05</td><td>Lorem ipsum dolor sit amet, consectetur adipsicing elit,</td><td>29</td></tr>
  <tr><td>06</td><td>Lorem ipsum dolor sit amet, consectetur adipsicing elit,</td><td>29</td></tr>
  <tr><td>07</td><td>Lorem ipsum dolor sit amet, consectetur adipsicing elit,</td><td>23</td></tr>
  <tr><td>08</td><td>Lorem ipsum dolor sit amet, consectetur adipsicing elit,</td><td>21</td></tr>
  <tr><td style="height:28px"></td><td></td><td></td></tr>
</table>
<div class="abs btn" style="left:229px;top:909px;width:76px;height:16px;font-size:7px;line-height:12px">View All Ranking</div>

<!-- top 3 cards -->
<section class="abs top3" style="left:96px"><h4>TOP 3 KILLER</h4><table><tr><th>Rank</th><th>Name</th><th>Team</th><th>Score</th></tr><tr><td>01</td><td>Marcus Hale</td><td>Lorem ipsum</td><td>58</td></tr><tr><td>02</td><td>Marcus Hale</td><td>Lorem ipsum</td><td>45</td></tr><tr><td>03</td><td>Marcus Hale</td><td>Lorem ipsum</td><td>43</td></tr></table></section>
<section class="abs top3" style="left:272px"><h4>TOP 3 CATCHER</h4><table><tr><th>Rank</th><th>Name</th><th>Team</th><th>Score</th></tr><tr><td>01</td><td>Marcus Hale</td><td>Lorem ipsum</td><td>58</td></tr><tr><td>02</td><td>Marcus Hale</td><td>Lorem ipsum</td><td>45</td></tr><tr><td>03</td><td>Marcus Hale</td><td>Lorem ipsum</td><td>43</td></tr></table></section>
<section class="abs top3" style="left:448px"><h4>TOP 3 DODGER</h4><table><tr><th>Rank</th><th>Name</th><th>Team</th><th>Score</th></tr><tr><td>01</td><td>Marcus Hale</td><td>Lorem ipsum</td><td>58</td></tr><tr><td>02</td><td>Marcus Hale</td><td>Lorem ipsum</td><td>45</td></tr><tr><td>03</td><td>Marcus Hale</td><td>Lorem ipsum</td><td>43</td></tr></table></section>
<div class="abs tape" style="left:232px;top:946px;transform:rotate(40deg)"></div>
<div class="abs tape" style="left:84px;top:1040px;transform:rotate(35deg)"></div>
<div class="abs tape" style="left:406px;top:946px;transform:rotate(40deg)"></div>
<div class="abs tape" style="left:260px;top:1040px;transform:rotate(35deg)"></div>
<div class="abs tape" style="left:582px;top:946px;transform:rotate(40deg)"></div>
<div class="abs tape" style="left:436px;top:1040px;transform:rotate(35deg)"></div>

<!-- sponsors -->
<div class="abs sponsors">
  <span class="sponsor">Copperpot Tavern</span>
  <span class="sponsor">Rivermark Lodge</span>
  <span class="sponsor">Seawick Market</span>
  <span class="sponsor">Ninecast</span>
  <span class="sponsor">Brightrail</span>
</div>

<footer class="abs foot"><span>Copyright © 2013 harbourdodge.com - All Rights Reserved</span><span>Privacy Policy &nbsp;|&nbsp; Term of uses</span></footer>

<!-- sidebar -->
<div class="abs like"><span class="tag">LIKE US ON</span><div class="word">Socialpage</div></div>
<aside class="abs register">
  <div class="kicker">★ Register Dodgeball ★</div>
  <div class="sub">Harbour dodge league</div>
  <p>Lorem ipsum dolor sit amet consectetur adip sicing elit, sed do euismod tempor incident magna aliqua...</p>
  <div class="field">Enter your email address...</div>
  <div class="field">Enter your password...</div>
  <div class="btn">Register Here</div>
</aside>
<aside class="abs plugin">
  <div class="ptitle"><span class="pdot"></span><span>Harbour Dodge League<br><small style="color:var(--muted);border:1px solid #ccc;padding:0 3px;font-size:5.5px">Like</small></span></div>
  <div style="margin-top:6px">2,971 people like Harbour Dodge League</div>
  <div class="avatars">
    <div><i></i>Ana</div><div><i></i>Ben</div><div><i></i>Sam</div><div><i></i>Dev</div>
    <div><i></i>Kit</div><div><i></i>Mia</div><div><i></i>Leo</div><div><i></i>Zoe</div>
  </div>
  <div style="margin-top:4px;color:var(--link-blue)">Social plugin</div>
</aside>
<div class="abs map-card"></div>
<div class="abs map-area" role="img" aria-label="Vintage map showing the league location"></div>
<div class="abs map-head">Location Map</div>
</body>
</html>
```